Business Card Design Project

Looking for a logo and business card for a Real State Business i will be opening. The name is not choosen yet , but will probably be RKT IMOVEIS.
I was thinking black and silver colors, but am open to nice ideas.
I did add a business card that i liked a lot, am looking for something like that, with logo in black or silver in a black card. The logo i was thinking in the letters RKT as i uploaded or something or little and cute buildings or a house...just ideas, can be any nice logo.
Updates

You guys can add other colors if you want, I like colors very "BRIGHT" and "open", like red, pink, strong colors. almost glow in the dark colors. lol

Designers,

I've increased more 88 dollars in the budget for 1st place cause I will want envelope designs... small and big sizes.

So 1st place is now U$248,00. 

No need to send the envelope designs right now... only the business cards designs.

Thank you.

Industry/Entity Type

Business

Requirements
Must have
• Patricia Souza Ramos

www.RKTimoveisx.com.br

+554193817462

patricia@rktimoveisx.com.br

```html
<!DOCTYPE html>
<html lang="pt-BR">
<head>
<meta charset="utf-8">
<title>Patricia Souza Ramos — Cartão de Visita</title>
<link rel="stylesheet" href="https://fonts.googleapis.com/css2?family=EB+Garamond:wght@400;500&display=swap">
<style>
  :root {
    --card-black: #000000;
    --text-white: #f4f4f4;
    --silver-light: #d9d9d9;
    --silver-mid: #9a9a9a;
    --silver-dark: #3a3a3a;
  }
  html, body {
    margin: 0;
    padding: 0;
    width: 1200px;
    height: 686px;
    overflow: hidden;
    background: var(--card-black);
  }
  .business-card {
    position: relative;
    width: 1200px;
    height: 686px;
    background: var(--card-black);
    font-family: "EB Garamond", "Garamond", serif;
    color: var(--text-white);
    overflow: hidden;
  }
  .floral-ornament {
    position: absolute;
    left: 0;
    top: 0;
    width: 230px;
    height: 686px;
  }
  .card-details {
    position: absolute;
    left: 230px;
    right: 0;
    top: 0;
    bottom: 0;
    text-align: center;
  }
  .holder-name {
    position: absolute;
    left: 0;
    right: 0;
    top: 118px;
    margin: 0;
    font-size: 68px;
    font-weight: 400;
    letter-spacing: 0.5px;
  }
  .contact-line {
    position: absolute;
    left: 0;
    right: 0;
    margin: 0;
    font-size: 34px;
    font-weight: 400;
  }
  .contact-web { top: 258px; }
  .contact-phone { top: 360px; }
  .contact-email { top: 474px; font-size: 38px; }
</style>
</head>
<body>
  <main class="business-card">
    <svg class="floral-ornament" viewBox="0 0 230 686" role="img" aria-label="Silver floral scroll ornament running down the left edge of the card">
      <defs>
        <linearGradient id="ornament-fade" x1="0" y1="0" x2="1" y2="0">
          <stop offset="0" stop-color="var(--silver-light)" stop-opacity="0.55"/>
          <stop offset="0.6" stop-color="var(--silver-mid)" stop-opacity="0.3"/>
          <stop offset="1" stop-color="var(--silver-dark)" stop-opacity="0"/>
        </linearGradient>
      </defs>
      <rect x="0" y="0" width="230" height="686" fill="url(#ornament-fade)"/>
    </svg>

    <section class="card-details">
      <h1 class="holder-name">Patricia Souza Ramos</h1>
      <p class="contact-line contact-web">www.RKTimoveisx.com.br</p>
      <p class="contact-line contact-phone">+554193817462</p>
      <p class="contact-line contact-email">patricia@rktimoveisx.com.br</p>
    </section>
  </main>
</body>
</html>
```